Brindle Wealth Management Flow Charts

I need help creating three flow charts for my businesses website. We want them to be simple but look professional. This is for a Wealth Management firm. I will attach a word document that has all of the descriptions for everything so you know what icons to use. We just want the chart to have an icon, the names of each step and the corresponding numbers. I will also include some examples of charts we liked as well. Once the winner is selected, we will need help with additional graphic design elements for our website ASAP.
Other font styles liked:
- Goudy Roman

```html
<!DOCTYPE html>
<html lang="en">
<head>
<meta charset="utf-8">
<title>Comprehensive Investment Management — Brindle Wealth Management</title>
<link rel="stylesheet" href="https://fonts.googleapis.com/css2?family=Oswald:wght@300;400&family=Sorts+Mill+Goudy&display=swap">
<style>
  :root {
    --bg: #ececec;
    --label: #6a6a6a;
    --icon: #585858;
    --dot: #8a8a8a;
    --disc: #f1f1f1;
    --orange: #f2a428;
    --green: #97bf2e;
    --cyan: #1eaac6;
    --blue: #1f5c93;
    --purple: #553b98;
    --pink: #cf3268;
    --footer: #3a3a3a;
  }
  * { margin: 0; padding: 0; box-sizing: border-box; }
  html, body { width: 1200px; height: 604px; overflow: hidden; background: var(--bg); }
  .canvas { position: relative; width: 1200px; height: 604px; background: var(--bg); }
  .flow { position: absolute; inset: 0; }
  .step-label {
    position: absolute;
    width: 200px;
    margin-left: -100px;
    text-align: center;
    font-family: "Oswald", sans-serif;
    font-weight: 300;
    font-size: 24px;
    line-height: 26px;
    color: var(--label);
  }
  .connector { position: absolute; width: 2px; margin-left: -1px; border-left: 1px dashed var(--dot); height: 63px; }
  .connector::before, .connector::after {
    content: ""; position: absolute; left: -3px; width: 5px; height: 5px; border-radius: 50%; background: var(--dot);
  }
  .connector::before { top: -2px; }
  .connector::after { bottom: -2px; }
  .section-title {
    position: absolute; left: 25px; top: 562px;
    font-family: "Sorts Mill Goudy", serif;
    font-size: 19px; letter-spacing: 10.6px; text-transform: uppercase;
    color: var(--footer);
  }
  .brand {
    position: absolute; right: 24px; top: 548px; width: 130px;
    text-align: center;
    font-family: "Oswald", sans-serif; font-weight: 300;
    font-size: 15px; line-height: 17px; letter-spacing: 1px;
    color: var(--footer);
  }
</style>
</head>
<body>
<main class="canvas">
  <svg class="flow" width="1200" height="604" viewBox="0 0 1200 604" aria-hidden="true">
    <defs>
      <linearGradient id="g1" x1="0" y1="1" x2="0" y2="0"><stop offset="0.45" stop-color="#f2a428"/><stop offset="0.6" stop-color="#97bf2e"/></linearGradient>
      <linearGradient id="g2" x1="0" y1="0" x2="0" y2="1"><stop offset="0.5" stop-color="#97bf2e"/><stop offset="0.62" stop-color="#1eaac6"/></linearGradient>
      <linearGradient id="g3" x1="0" y1="1" x2="0" y2="0"><stop offset="0.45" stop-color="#1eaac6"/><stop offset="0.6" stop-color="#1f5c93"/></linearGradient>
      <linearGradient id="g4" x1="0" y1="0" x2="0" y2="1"><stop offset="0.5" stop-color="#1f5c93"/><stop offset="0.62" stop-color="#553b98"/></linearGradient>
      <linearGradient id="g5" x1="0" y1="1" x2="0" y2="0"><stop offset="0.45" stop-color="#553b98"/><stop offset="0.6" stop-color="#cf3268"/></linearGradient>
      <filter id="shade" x="-30%" y="-30%" width="160%" height="160%"><feDropShadow dx="0" dy="3" stdDeviation="4" flood-opacity="0.28"/></filter>
    </defs>

    <g class="ribbon" fill="none" stroke-width="58" stroke-linecap="round">
      <path d="M150,350 C230,320 200,250 300,215" stroke="url(#g1)"/>
      <path d="M340,215 C430,250 400,330 490,350" stroke="url(#g2)"/>
      <path d="M525,350 C605,320 575,250 675,215" stroke="url(#g3)"/>
      <path d="M715,215 C805,250 775,330 865,350" stroke="url(#g4)"/>
      <path d="M900,350 C980,320 950,250 1050,215" stroke="url(#g5)"/>
    </g>

    <g class="rings" filter="url(#shade)">
      <circle cx="132" cy="374" r="67" fill="var(--orange)"/>
      <circle cx="319" cy="187" r="67" fill="var(--green)"/>
      <circle cx="506" cy="374" r="67" fill="var(--cyan)"/>
      <circle cx="694" cy="187" r="67" fill="var(--blue)"/>
      <circle cx="881" cy="374" r="67" fill="var(--purple)"/>
      <circle cx="1068" cy="187" r="67" fill="var(--pink)"/>
    </g>
    <g class="discs" fill="var(--disc)" filter="url(#shade)">
      <circle cx="132" cy="374" r="49"/>
      <circle cx="319" cy="187" r="49"/>
      <circle cx="506" cy="374" r="49"/>
      <circle cx="694" cy="187" r="49"/>
      <circle cx="881" cy="374" r="49"/>
      <circle cx="1068" cy="187" r="49"/>
    </g>

    <!-- risk gauge -->
    <g class="icon icon-gauge" transform="translate(132 386)">
      <path d="M-29,0 A29,29 0 0 1 29,0 L17,0 A17,17 0 0 0 -17,0 Z" fill="#7a7a7a"/>
      <path d="M-20,-21 A29,29 0 0 1 20,-21 L12,-12 A17,17 0 0 0 -12,-12 Z" fill="#b8b8b8"/>
      <line x1="0" y1="0" x2="-11" y2="-7" stroke="#222" stroke-width="2.4" stroke-linecap="round"/>
      <circle cx="0" cy="0" r="3" fill="#222"/>
      <text x="0" y="-31" font-family="Oswald, sans-serif" font-size="5" text-anchor="middle" fill="#444">MEDIUM</text>
      <text x="-36" y="-3" font-family="Oswald, sans-serif" font-size="5" text-anchor="middle" fill="#444">LOW</text>
      <text x="36" y="-3" font-family="Oswald, sans-serif" font-size="5" text-anchor="middle" fill="#444">HIGH</text>
      <text x="0" y="13" font-family="Oswald, sans-serif" font-weight="400" font-size="9" text-anchor="middle" fill="#222">RISK</text>
    </g>

    <!-- funnel -->
    <g class="icon icon-funnel" transform="translate(319 187)" fill="none" stroke="var(--icon)" stroke-width="1.8">
      <circle cx="0" cy="-18" r="8"/>
      <path d="M-21,-10 H21 V-6 L6,10 V14 H-6 V10 L-21,-6 Z"/>
      <circle cx="0" cy="22" r="9"/>
      <path d="M-29,-14 V10 M-22,-8 V18 M22,-8 V18 M29,-14 V10"/>
      <circle cx="-29" cy="12" r="2"/><circle cx="-22" cy="20" r="2"/><circle cx="22" cy="20" r="2"/><circle cx="29" cy="12" r="2"/>
      <text x="0" y="-14" font-family="Oswald, sans-serif" font-size="11" text-anchor="middle" fill="var(--icon)" stroke="none">$</text>
      <text x="0" y="26" font-family="Oswald, sans-serif" font-size="12" text-anchor="middle" fill="var(--icon)" stroke="none">$</text>
    </g>

    <!-- allocation pie -->
    <g class="icon icon-pie" transform="translate(506 376)" stroke="var(--icon)" stroke-width="1.6">
      <path d="M0,-30 A30,30 0 0 0 -21,21 L-10,10 A14,14 0 0 1 0,-14 Z" fill="#d6d6d6"/>
      <path d="M-21,21 A30,30 0 0 0 0,30 L0,14 A14,14 0 0 1 -10,10 Z" fill="#9a9a9a"/>
      <path d="M0,30 A30,30 0 0 0 30,0 L14,0 A14,14 0 0 1 0,14 Z" fill="#6a6a6a"/>
      <path d="M2,-32 A32,32 0 0 1 32,-2 L2,-2 Z" fill="#fafafa"/>
      <path d="M20,-24 L30,-36 H36" fill="none"/>
      <circle cx="0" cy="0" r="10" fill="#f5f5f5"/>
      <text x="0" y="5" font-family="Oswald, sans-serif" font-size="14" text-anchor="middle" fill="var(--icon)" stroke="none">$</text>
    </g>

    <!-- hourglass -->
    <g class="icon icon-hourglass" transform="translate(694 187)" fill="var(--icon)">
      <rect x="-19" y="-25" width="38" height="3"/>
      <rect x="-19" y="22" width="38" height="3"/>
      <path d="M-14,-21 H14 C14,-8 4,-4 3,0 C4,4 14,8 14,21 H-14 C-14,8 -4,4 -3,0 C-4,-4 -14,-8 -14,-21 Z"/>
      <circle cx="0" cy="-10" r="5" fill="none" stroke="#f1f1f1" stroke-width="1.4"/>
      <path d="M-3,14 A5,5 0 0 1 4,7" fill="none" stroke="#f1f1f1" stroke-width="1.4"/>
    </g>

    <!-- network -->
    <g class="icon icon-network" transform="translate(881 374)" fill="none" stroke="var(--icon)" stroke-width="2">
      <rect x="-6" y="-6" width="12" height="12"/>
      <rect x="-2" y="-2" width="4" height="4" fill="var(--icon)"/>
      <path d="M0,-6 V-15 M0,6 V15 M-6,0 H-15 M6,0 H15 M-5,-5 L-11,-11 M5,-5 L11,-11 M-5,5 L-11,11 M5,5 L11,11"/>
      <circle cx="0" cy="-20" r="4"/><circle cx="0" cy="20" r="4"/><circle cx="-20" cy="0" r="4"/><circle cx="20" cy="0" r="4"/>
      <circle cx="-15" cy="-15" r="4"/><circle cx="15" cy="-15" r="4"/><circle cx="-15" cy="15" r="4"/><circle cx="15" cy="15" r="4"/>
    </g>

    <!-- coaching presenter -->
    <g class="icon icon-coaching" transform="translate(1068 187)" fill="none" stroke="var(--icon)" stroke-width="1.8">
      <rect x="-4" y="-24" width="30" height="30"/>
      <circle cx="10" cy="-9" r="9"/>
      <text x="10" y="-4" font-family="Oswald, sans-serif" font-size="13" text-anchor="middle" fill="var(--icon)" stroke="none">$</text>
      <circle cx="-20" cy="-21" r="4"/>
      <path d="M-27,1 V-13 H-13 V1 M-22,-13 V17 M-18,-13 V17 M-13,-8 L-4,-12"/>
      <circle cx="-8" cy="8" r="4"/><circle cx="5" cy="8" r="4"/><circle cx="18" cy="8" r="4"/>
      <path d="M-14,22 C-14,14 -2,14 -2,22 Z M-1,22 C-1,14 11,14 11,22 Z M12,22 C12,14 24,14 24,22 Z"/>
    </g>
  </svg>

  <div class="step-label" style="left:134px; top:120px">Risk Tolerance<br>Assessment</div>
  <div class="connector" style="left:132px; top:199px"></div>

  <div class="step-label" style="left:317px; top:396px">Investment<br>Decisions</div>
  <div class="connector" style="left:319px; top:302px"></div>

  <div class="step-label" style="left:502px; top:120px">Asset<br>Allocation</div>
  <div class="connector" style="left:501px; top:199px"></div>

  <div class="step-label" style="left:695px; top:396px">Tax<br>Mitigation</div>
  <div class="connector" style="left:694px; top:302px"></div>

  <div class="step-label" style="left:879px; top:120px">Distribution<br>Strategy</div>
  <div class="connector" style="left:881px; top:199px"></div>

  <div class="step-label" style="left:1068px; top:370px">Behavior<br>Finance<br>Coaching</div>
  <div class="connector" style="left:1068px; top:302px"></div>

  <h1 class="section-title">Comprehensive Investment Management</h1>
  <p class="brand">Brindle Wealth Management</p>
</main>
</body>
</html>
```